Accountancy practice needs a wordpress website redesign for growth

We are a growing accountancy practice - headcount and revenues have doubled in the last 2 years. We are continuing to grow. We only had a website made around 12 months ago but the company we used offered very little in terms of creativity and ideas of how to make it look modern and eye-catching. We want to redesign the website to make it look premium and professional because we are starting to launch more marketing and drive more traffic to the site.

The current website is www.tolvardaccountants.co.uk. The website was built in wordpress.

The logo has been uploaded. The main 2 colour hex codes are: 0E74BC and 14A79D.

We are open to changing the fonts in the website and welcome suggestions for this too.

Following on from this we will launch a project to design brochures and one-page flyers that we can fill with useful information about what we do and also create lead-generators to download from the website. So the design of the website will influence the overall brand and feel of all of the marketing collateral.

Target Market(s)

Property businesses and entrepreneurial, growth mindset clients

Industry/Entity Type

Accountancy

Number of Pages Required

3 page

Font styles to use
Sans Serif

Colors

Designer to choose colors to be used in the design.

Requirements
Must have
• A modern and professional feel. 3 fonts - most websites seem to use 3 different fonts now and I like this. We have our green and blue colours but I do not want too much of this all over the site, stick to blacks, whites and greys with the blue and green used for emphasis and accents.
Nice to have
• The coloured spaces should have some "depth" to them, eg a small pattern in the white spaces so its not just a solid whie background.

```html
<!DOCTYPE html>
<html lang="en">
<head>
<meta charset="utf-8">
<title>Tolvard Accountants – Services</title>
<link href="https://fonts.googleapis.com/css2?family=Oswald:wght@400;500&family=Open+Sans:wght@400;600&display=swap" rel="stylesheet">
<style>
:root{
  --blue:#0E74BC;
  --teal:#14A79D;
  --ink:#1b1e22;
  --text:#3c4045;
  --muted:#6d7277;
  --dark:#1f2429;
  --footer:#1d2227;
  --line:#e3e6e9;
  --tick-bg:#eef1f3;
  --white:#ffffff;
}
*{box-sizing:border-box;margin:0;padding:0}
html,body{width:1200px;height:4586px;overflow:hidden}
body{position:relative;background:var(--white);font-family:"Open Sans",Arial,sans-serif;color:var(--text)}
.oswald{font-family:"Oswald",Arial Narrow,sans-serif;font-weight:500}
section,header,footer{position:relative;width:1200px;overflow:hidden}

/* header */
.site-header{height:75px;background:var(--white);box-shadow:0 1px 6px rgba(0,0,0,.06);z-index:2}
.brand{position:absolute;left:64px;top:22px;display:flex;align-items:center;gap:10px}
.brand-mark{width:22px;height:22px;background:var(--blue)}
.brand-name{font-family:"Oswald",sans-serif;font-weight:500;font-size:22px;color:var(--blue);letter-spacing:.5px;text-transform:uppercase}
.main-nav{position:absolute;left:425px;top:28px;display:flex;gap:40px}
.main-nav a{font-family:"Oswald",sans-serif;font-weight:500;font-size:12px;color:var(--ink);text-decoration:none;letter-spacing:.3px}
.header-btn{position:absolute;top:17px;height:43px;display:flex;align-items:center;justify-content:center;font-family:"Oswald",sans-serif;font-weight:500;font-size:14px;color:#fff;border-radius:3px}
.btn-touch{left:869px;width:124px;background:var(--blue)}
.btn-login{left:1006px;width:116px;background:var(--teal)}

/* hero */
.hero{height:393px;background:linear-gradient(90deg,#07163a 0%,#0a2456 45%,#0d3a8a 100%)}
.hero-visual{position:absolute;left:620px;top:0;width:580px;height:393px;background:radial-gradient(ellipse at 60% 45%,rgba(60,160,255,.65) 0%,rgba(20,90,200,.35) 40%,rgba(10,36,86,0) 75%)}
.hero-title{position:absolute;left:96px;top:160px;font-family:"Oswald",sans-serif;font-weight:500;font-size:50px;color:#fff;line-height:1}
.hero-title .mark{background:linear-gradient(transparent 58%,rgba(120,190,245,.75) 58%)}

/* services */
.services{height:2112px;background:var(--white)}
.section-title{position:absolute;left:0;width:1200px;text-align:center;font-family:"Oswald",sans-serif;font-weight:500;font-size:38px;line-height:44px;color:var(--ink)}
.section-lead{position:absolute;left:250px;width:700px;text-align:center;font-size:18px;line-height:28px;color:var(--ink)}
.services .section-title{top:68px}
.services .section-lead{top:140px}
.service{position:absolute;width:440px}
.service-photo{width:412px;height:185px}
.service h3{font-family:"Oswald",sans-serif;font-weight:500;font-size:19px;color:var(--ink);margin-top:22px}
.service p{font-size:13.5px;line-height:24px;color:var(--muted);margin-top:12px;width:420px}
.ticks{list-style:none;margin-top:18px}
.ticks li{position:relative;padding-left:30px;font-size:14px;line-height:23px;color:var(--text);margin-bottom:13px;width:430px}
.ticks li svg{position:absolute;left:0;top:3px}
.col-a{left:142px}
.col-b{left:611px}
.row-1{top:235px}
.row-2{top:926px}
.row-3{top:1432px}
.btn{position:absolute;height:46px;display:flex;align-items:center;justify-content:center;background:var(--teal);color:#fff;font-family:"Oswald",sans-serif;font-weight:500;font-size:14px;letter-spacing:.4px;box-shadow:0 6px 16px rgba(20,167,157,.3)}
.services .btn{left:498px;top:1978px;width:203px}

/* steps */
.steps{height:726px;background:var(--dark)}
.steps .section-title{top:80px;color:#fff}
.steps .section-lead{top:150px;left:270px;width:660px;color:#fff;font-weight:600;font-size:17.5px}
.step{position:absolute;top:278px;width:260px;text-align:center}
.step-icon{position:relative;width:80px;height:80px;margin:0 auto;border-radius:50%;background:var(--blue);display:flex;align-items:center;justify-content:center}
.step-num{position:absolute;right:2px;bottom:-2px;width:18px;height:18px;border-radius:50%;background:#fff;color:var(--blue);font-size:10px;font-weight:600;display:flex;align-items:center;justify-content:center}
.step h3{font-family:"Oswald",sans-serif;font-weight:500;font-size:19px;color:#fff;margin-top:30px}
.step p{font-size:14.5px;line-height:25.5px;color:#e9ecef;margin-top:12px;padding:0 6px}
.step-link{position:absolute;top:317px;width:150px;border-top:2px dotted rgba(20,167,157,.6)}
.steps .btn{left:502px;top:596px;width:203px}

/* who we help */
.help{height:887px;background:var(--white)}
.help .section-title{top:80px}
.help .section-lead{top:148px}
.tab-row{position:absolute;left:199px;top:254px;width:784px;height:140px;border-bottom:1px solid var(--line)}
.tab{position:absolute;top:0;width:168px;height:140px;display:flex;flex-direction:column;align-items:center;justify-content:center;gap:12px;text-align:center;font-family:"Oswald",sans-serif;font-weight:500;font-size:16px;line-height:20px;color:var(--ink)}
.tab.active{background:#fff;box-shadow:0 4px 18px rgba(0,0,0,.09);border-bottom:3px solid var(--blue)}
.help h3{position:absolute;top:426px;left:0;width:1200px;text-align:center;font-family:"Oswald",sans-serif;font-weight:500;font-size:25px;color:var(--ink)}
.help-copy{position:absolute;left:255px;width:690px;text-align:center;font-size:14px;line-height:24px;color:var(--text)}
.help-copy.strong{font-weight:600;color:var(--ink)}
.help .btn{left:500px;top:4073px;width:203px;top:767px}

/* footer */
.site-footer{height:393px;background:var(--footer);color:#aeb4ba}
.site-footer .brand{left:157px;top:98px}
.foot-address{position:absolute;left:157px;top:155px;font-size:13px;line-height:20px;color:#aeb4ba}
.foot-contact{position:absolute;left:157px;display:flex;align-items:center;gap:14px;font-size:13px;color:#d3d7db}
.foot-contact .dot{width:18px;height:18px;border-radius:50%;background:#2e353c;display:flex;align-items:center;justify-content:center}
.foot-col{position:absolute;top:96px}
.foot-col h4{font-family:"Oswald",sans-serif;font-weight:500;font-size:14px;color:#fff;margin-bottom:16px;letter-spacing:.3px}
.foot-col a{display:block;font-size:12.5px;line-height:29px;color:#aeb4ba;text-decoration:none}
.foot-bottom{position:absolute;left:157px;top:336px;width:890px;height:24px;display:flex;align-items:center}
.copyright{font-size:12.5px;color:#aeb4ba}
.badge-a{position:absolute;left:382px;top:0;width:66px;height:28px;background:#fff;border-radius:2px}
.badge-b{position:absolute;left:487px;top:0;width:100px;height:28px;background:#3a4249;border-radius:2px}
.social{position:absolute;right:0;top:0;display:flex;gap:18px}
.social span{width:22px;height:22px;border-radius:50%;background:#2e353c}
</style>
</head>
<body>

<header class="site-header">
  <div class="brand"><span class="brand-mark"></span><span class="brand-name">Tolvard Accountants</span></div>
  <nav class="main-nav">
    <a href="#">ABOUT US</a><a href="#">WHO WE HELP</a><a href="#">THOUGHTS</a><a href="#">SWITCHING ACCOUNTANTS</a>
  </nav>
  <a class="header-btn btn-touch">GET IN TOUCH</a>
  <a class="header-btn btn-login">LOGIN</a>
</header>

<section class="hero">
  <div class="hero-visual" role="img" aria-label="Hand holding a glowing rising growth chart over financial figures"></div>
  <h1 class="hero-title"><span class="mark">Services</span> we provide</h1>
</section>

<section class="services">
  <h2 class="section-title">What we do for you</h2>
  <p class="section-lead">You need an accountant that you can rely on and trust. From VAT to full company accounts &amp; payroll you can be assured that we are experts in our field.</p>

  <article class="service col-a row-1">
    <div class="service-photo" role="img" aria-label="Businesswoman working at a laptop in a bright office" style="background:linear-gradient(120deg,#f4f3f0,#d9d3cb 55%,#8c7f72)"></div>
    <h3>Company Secretarial</h3>
    <p>It is vital that you spend your time on running and developing your business and we want to help make that happen. We offer a range of company secretarial services.</p>
    <ul class="ticks">
      <li><svg width="17" height="17" viewBox="0 0 17 17"><circle cx="8.5" cy="8.5" r="8.5" fill="#eef1f3"/><path d="M5 8.7l2.3 2.3L12 6.3" stroke="#14A79D" stroke-width="1.6" fill="none"/></svg>Company formation</li>
      <li><svg width="17" height="17" viewBox="0 0 17 17"><circle cx="8.5" cy="8.5" r="8.5" fill="#eef1f3"/><path d="M5 8.7l2.3 2.3L12 6.3" stroke="#14A79D" stroke-width="1.6" fill="none"/></svg>Dissolution of unwanted companies</li>
      <li><svg width="17" height="17" viewBox="0 0 17 17"><circle cx="8.5" cy="8.5" r="8.5" fill="#eef1f3"/><path d="M5 8.7l2.3 2.3L12 6.3" stroke="#14A79D" stroke-width="1.6" fill="none"/></svg>Managing company liquidations</li>
      <li><svg width="17" height="17" viewBox="0 0 17 17"><circle cx="8.5" cy="8.5" r="8.5" fill="#eef1f3"/><path d="M5 8.7l2.3 2.3L12 6.3" stroke="#14A79D" stroke-width="1.6" fill="none"/></svg>Preparation of board minutes, resolutions and maintaining statutory books</li>
      <li><svg width="17" height="17" viewBox="0 0 17 17"><circle cx="8.5" cy="8.5" r="8.5" fill="#eef1f3"/><path d="M5 8.7l2.3 2.3L12 6.3" stroke="#14A79D" stroke-width="1.6" fill="none"/></svg>Preparing and filing annual Confirmation Statements and maintaining PSC details</li>
      <li><svg width="17" height="17" viewBox="0 0 17 17"><circle cx="8.5" cy="8.5" r="8.5" fill="#eef1f3"/><path d="M5 8.7l2.3 2.3L12 6.3" stroke="#14A79D" stroke-width="1.6" fill="none"/></svg>Customising Articles of Associations</li>
      <li><svg width="17" height="17" viewBox="0 0 17 17"><circle cx="8.5" cy="8.5" r="8.5" fill="#eef1f3"/><path d="M5 8.7l2.3 2.3L12 6.3" stroke="#14A79D" stroke-width="1.6" fill="none"/></svg>Executing changes in company and group structures</li>
    </ul>
  </article>

  <article class="service col-b row-1">
    <div class="service-photo" role="img" aria-label="Note card with VAT written on it beside a coffee cup" style="background:linear-gradient(120deg,#d8cdb9,#b9a98e 50%,#c94a52)"></div>
    <h3>VAT</h3>
    <p>VAT can certainly be a complex and overwhelming subject if you are not sure what you are doing. We provide VAT services ensuring your VAT returns are filed as required.</p>
    <ul class="ticks">
      <li><svg width="17" height="17" viewBox="0 0 17 17"><circle cx="8.5" cy="8.5" r="8.5" fill="#eef1f3"/><path d="M5 8.7l2.3 2.3L12 6.3" stroke="#14A79D" stroke-width="1.6" fill="none"/></svg>Preparation and filing of quarterly VAT returns</li>
      <li><svg width="17" height="17" viewBox="0 0 17 17"><circle cx="8.5" cy="8.5" r="8.5" fill="#eef1f3"/><path d="M5 8.7l2.3 2.3L12 6.3" stroke="#14A79D" stroke-width="1.6" fill="none"/></svg>Partial exemption</li>
      <li><svg width="17" height="17" viewBox="0 0 17 17"><circle cx="8.5" cy="8.5" r="8.5" fill="#eef1f3"/><path d="M5 8.7l2.3 2.3L12 6.3" stroke="#14A79D" stroke-width="1.6" fill="none"/></svg>Flat rate scheme</li>
      <li><svg width="17" height="17" viewBox="0 0 17 17"><circle cx="8.5" cy="8.5" r="8.5" fill="#eef1f3"/><path d="M5 8.7l2.3 2.3L12 6.3" stroke="#14A79D" stroke-width="1.6" fill="none"/></svg>Cash accounting</li>
      <li><svg width="17" height="17" viewBox="0 0 17 17"><circle cx="8.5" cy="8.5" r="8.5" fill="#eef1f3"/><path d="M5 8.7l2.3 2.3L12 6.3" stroke="#14A79D" stroke-width="1.6" fill="none"/></svg>Dealing with VAT enquiries by HMRC VAT on property investments</li>
      <li><svg width="17" height="17" viewBox="0 0 17 17"><circle cx="8.5" cy="8.5" r="8.5" fill="#eef1f3"/><path d="M5 8.7l2.3 2.3L12 6.3" stroke="#14A79D" stroke-width="1.6" fill="none"/></svg>VAT on property development</li>
      <li><svg width="17" height="17" viewBox="0 0 17 17"><circle cx="8.5" cy="8.5" r="8.5" fill="#eef1f3"/><path d="M5 8.7l2.3 2.3L12 6.3" stroke="#14A79D" stroke-width="1.6" fill="none"/></svg>Optimising group structures for VAT</li>
      <li><svg width="17" height="17" viewBox="0 0 17 17"><circle cx="8.5" cy="8.5" r="8.5" fill="#eef1f3"/><path d="M5 8.7l2.3 2.3L12 6.3" stroke="#14A79D" stroke-width="1.6" fill="none"/></svg>Cross-border VAT</li>
    </ul>
  </article>

  <article class="service col-a row-2">
    <div class="service-photo" role="img" aria-label="Smiling shop owner in an apron standing in a store" style="background:linear-gradient(120deg,#6b4a2a,#b8894f 50%,#3f5f7a)"></div>
    <h3>Bookkeeping</h3>
    <p>The heartbeat of any business accounts is their bookkeeping. We take this away from your daily to-do list ensuing your accounts are always taken care of.</p>
    <ul class="ticks">
      <li><svg width="17" height="17" viewBox="0 0 17 17"><circle cx="8.5" cy="8.5" r="8.5" fill="#eef1f3"/><path d="M5 8.7l2.3 2.3L12 6.3" stroke="#14A79D" stroke-width="1.6" fill="none"/></svg>Monthly or quarterly bookkeeping</li>
      <li><svg width="17" height="17" viewBox="0 0 17 17"><circle cx="8.5" cy="8.5" r="8.5" fill="#eef1f3"/><path d="M5 8.7l2.3 2.3L12 6.3" stroke="#14A79D" stroke-width="1.6" fill="none"/></svg>Maintaining nominal, purchase and sales ledgers</li>
      <li><svg width="17" height="17" viewBox="0 0 17 17"><circle cx="8.5" cy="8.5" r="8.5" fill="#eef1f3"/><path d="M5 8.7l2.3 2.3L12 6.3" stroke="#14A79D" stroke-width="1.6" fill="none"/></svg>Monthly, quarterly bank reconciliations</li>
    </ul>
  </article>

  <article class="service col-b row-2">
    <div class="service-photo" role="img" aria-label="Business partners meeting around a table with laptops" style="background:linear-gradient(120deg,#cfc6bb,#9c8e80 50%,#5d6670)"></div>
    <h3>Sole Trader &amp; Partnerships</h3>
    <p>Removing the stress of your accounts when you are constantly busy on other aspects of your business is what we do best.</p>
    <ul class="ticks">
      <li><svg width="17" height="17" viewBox="0 0 17 17"><circle cx="8.5" cy="8.5" r="8.5" fill="#eef1f3"/><path d="M5 8.7l2.3 2.3L12 6.3" stroke="#14A79D" stroke-width="1.6" fill="none"/></svg>Preparation of sole trader accounts</li>
      <li><svg width="17" height="17" viewBox="0 0 17 17"><circle cx="8.5" cy="8.5" r="8.5" fill="#eef1f3"/><path d="M5 8.7l2.3 2.3L12 6.3" stroke="#14A79D" stroke-width="1.6" fill="none"/></svg>Assistance with partnership compliant requirements</li>
      <li><svg width="17" height="17" viewBox="0 0 17 17"><circle cx="8.5" cy="8.5" r="8.5" fill="#eef1f3"/><path d="M5 8.7l2.3 2.3L12 6.3" stroke="#14A79D" stroke-width="1.6" fill="none"/></svg>Preparation of partner accounts &amp; allocation of profit percentages</li>
    </ul>
  </article>

  <article class="service col-a row-3">
    <div class="service-photo" role="img" aria-label="Hands holding a phone beside a laptop on a white desk" style="background:linear-gradient(120deg,#f2f3f4,#c9ccd0 55%,#6f747a)"></div>
    <h3>Company Accounts</h3>
    <p>As company directors ensuring all the accounts are filed correctly is all part of your responsibilities. Having professional accountants on your side to ensure this is done correctly is a must for every limited company.</p>
    <ul class="ticks">
      <li><svg width="17" height="17" viewBox="0 0 17 17"><circle cx="8.5" cy="8.5" r="8.5" fill="#eef1f3"/><path d="M5 8.7l2.3 2.3L12 6.3" stroke="#14A79D" stroke-width="1.6" fill="none"/></svg>Preparation of accounts in formats required</li>
      <li><svg width="17" height="17" viewBox="0 0 17 17"><circle cx="8.5" cy="8.5" r="8.5" fill="#eef1f3"/><path d="M5 8.7l2.3 2.3L12 6.3" stroke="#14A79D" stroke-width="1.6" fill="none"/></svg>Ensure accounts meet latest accountancy standards</li>
      <li><svg width="17" height="17" viewBox="0 0 17 17"><circle cx="8.5" cy="8.5" r="8.5" fill="#eef1f3"/><path d="M5 8.7l2.3 2.3L12 6.3" stroke="#14A79D" stroke-width="1.6" fill="none"/></svg>Constant communication for efficient enquiries</li>
      <li><svg width="17" height="17" viewBox="0 0 17 17"><circle cx="8.5" cy="8.5" r="8.5" fill="#eef1f3"/><path d="M5 8.7l2.3 2.3L12 6.3" stroke="#14A79D" stroke-width="1.6" fill="none"/></svg>Accurate and timely accounts</li>
    </ul>
  </article>

  <article class="service col-b row-3">
    <div class="service-photo" role="img" aria-label="Hand with pen over a glowing tax chart display" style="background:linear-gradient(120deg,#0b1f3a,#1d4f7a 55%,#c9a24a)"></div>
    <h3>Corporate Tax &amp; Planning</h3>
    <p>We take great pride in ensuring all our clients are set up in the most tax efficient way. We work to understand the big picture of your business and how we can help you with the best and most efficient solutions.</p>
    <ul class="ticks">
      <li><svg width="17" height="17" viewBox="0 0 17 17"><circle cx="8.5" cy="8.5" r="8.5" fill="#eef1f3"/><path d="M5 8.7l2.3 2.3L12 6.3" stroke="#14A79D" stroke-width="1.6" fill="none"/></svg>Preparation and filing corporation tax return</li>
      <li><svg width="17" height="17" viewBox="0 0 17 17"><circle cx="8.5" cy="8.5" r="8.5" fill="#eef1f3"/><path d="M5 8.7l2.3 2.3L12 6.3" stroke="#14A79D" stroke-width="1.6" fill="none"/></svg>Managing R&amp;D tax and other reliefs through our partners</li>
      <li><svg width="17" height="17" viewBox="0 0 17 17"><circle cx="8.5" cy="8.5" r="8.5" fill="#eef1f3"/><path d="M5 8.7l2.3 2.3L12 6.3" stroke="#14A79D" stroke-width="1.6" fill="none"/></svg>Maximising capital allowance claims</li>
      <li><svg width="17" height="17" viewBox="0 0 17 17"><circle cx="8.5" cy="8.5" r="8.5" fill="#eef1f3"/><path d="M5 8.7l2.3 2.3L12 6.3" stroke="#14A79D" stroke-width="1.6" fill="none"/></svg>Business structuring</li>
    </ul>
  </article>

  <a class="btn">VIEW MORE SERVICES</a>
</section>

<section class="steps">
  <h2 class="section-title">What you need to do now</h2>
  <p class="section-lead">Donec vitae vestibulum risus, et accumsan est. Donec malesuada, nisi vel dictum ornare, mi metus pharetra orci, malesuada tempus felis odio vel ex. Vivamus nec ligula aliquet risus.</p>

  <div class="step-link" style="left:362px"></div>
  <div class="step-link" style="left:679px"></div>

  <div class="step" style="left:151px">
    <div class="step-icon">
      <svg width="36" height="36" viewBox="0 0 36 36" fill="none" stroke="#fff" stroke-width="1.6"><circle cx="18" cy="11" r="6"/><path d="M7 31c0-6 5-10 11-10s11 4 11 10"/></svg>
      <span class="step-num">1</span>
    </div>
    <h3>Get in touch</h3>
    <p>Book a call with us where we can get to know you better, understand your business, your challenges &amp; where you want to get to in order to see if we're a good fit to work with you.</p>
  </div>

  <div class="step" style="left:468px">
    <div class="step-icon">
      <svg width="36" height="36" viewBox="0 0 36 36" fill="none" stroke="#fff" stroke-width="1.6"><path d="M18 5a9 9 0 0 0-5 16.5V25h10v-3.5A9 9 0 0 0 18 5z"/><path d="M14 29h8M15 32h6"/></svg>
      <span class="step-num">2</span>
    </div>
    <h3>Get a plan</h3>
    <p>We'll put together a plan to help you to get your structure right, start to manage your finances better, find ways to pay less tax and take the stress of your accounts away.</p>
  </div>

  <div class="step" style="left:785px">
    <div class="step-icon">
      <svg width="36" height="36" viewBox="0 0 36 36" fill="none" stroke="#fff" stroke-width="1.6"><rect x="7" y="9" width="22" height="20" rx="2"/><path d="M12 19l4 4 8-8"/></svg>
      <span class="step-num">3</span>
    </div>
    <h3>Get going</h3>
    <p>We take over everything from your old accountant, get you set up on our systems &amp; meet your client success team. We'll set out timeframes, etc. &amp; help you get to new level of success.</p>
  </div>

  <a class="btn">BOOK A CALL</a>
</section>

<section class="help">
  <h2 class="section-title">Who we help?</h2>
  <p class="section-lead">You need an accountant that you can rely on and trust. From VAT to full company accounts &amp; payroll you can be assured that we are experts in our field.</p>

  <div class="tab-row">
    <div class="tab" style="left:37px">
      <svg width="44" height="44" viewBox="0 0 44 44" fill="none" stroke="#0E74BC" stroke-width="1.6"><circle cx="12" cy="12" r="4"/><circle cx="32" cy="12" r="4"/><path d="M5 30c0-5 3-8 7-8s7 3 7 8M25 30c0-5 3-8 7-8s7 3 7 8"/><rect x="15" y="30" width="14" height="8"/></svg>
      <span>Consultants</span>
    </div>
    <div class="tab active" style="left:226px">
      <svg width="44" height="44" viewBox="0 0 44 44" fill="none" stroke="#0E74BC" stroke-width="1.6"><rect x="10" y="8" width="16" height="30"/><rect x="26" y="18" width="10" height="20"/><path d="M14 14h3M19 14h3M14 20h3M19 20h3M14 26h3M19 26h3M6 38h34"/></svg>
      <span>Property investor<br>&amp; developer</span>
    </div>
    <div class="tab" style="left:404px">
      <svg width="44" height="44" viewBox="0 0 44 44" fill="none" stroke="#0E74BC" stroke-width="1.6"><path d="M12 6v10a7 7 0 0 0 14 0V6"/><path d="M19 23v7a7 7 0 0 0 14 0v-4"/><circle cx="33" cy="23" r="3"/></svg>
      <span>Medical<br>Professionals</span>
    </div>
    <div class="tab" style="left:586px">
      <svg width="44" height="44" viewBox="0 0 44 44" fill="none" stroke="#0E74BC" stroke-width="1.6"><path d="M4 22l8-8 6 3 6-3 6 3 10 5"/><path d="M12 24l7 7 4-3 4 3 6-6"/><circle cx="30" cy="10" r="5"/><path d="M27.5 10l2 2 3-3.5"/></svg>
      <span>Buying or<br>Selling a business</span>
    </div>
  </div>

  <h3>Property investor &amp; Developer</h3>
  <p class="help-copy strong" style="top:480px">If you are buying properties and developing your own projects and portfolio, then we can help you do it tax-efficiently. Get unlimited access to our partners who have been through the same things you are and have the experience to share with you.</p>
  <p class="help-copy" style="top:560px">You are working hard to find deals that stack, investments that make a solid return and managing your build-outs – yet there is a niggling feeling that something about the way you are set up is not quite right. Do you feel like your accountant does not have the specialist knowledge or in-the-trenches experience to know how to help you optimise your operations?</p>
  <p class="help-copy" style="top:670px">We've had a lot of people like you come and say their accountant said, "just get started, we'll worry about that later". The problem here is that property transactions are not something that can be easily undone and changed.</p>

  <a class="btn">FIND OUT MORE</a>
</section>

<footer class="site-footer">
  <div class="brand"><span class="brand-mark"></span><span class="brand-name">Tolvard Accountants</span></div>
  <p class="foot-address">12 Harrow Lane, Ashmere,<br>DA9 4RT</p>
  <div class="foot-contact" style="top:210px"><span class="dot"><svg width="10" height="8" viewBox="0 0 10 8" fill="none" stroke="#aeb4ba"><rect x=".5" y=".5" width="9" height="7"/><path d="M.5 .5l4.5 4 4.5-4"/></svg></span>info@tolvardaccountants.co.uk</div>
  <div class="foot-contact" style="top:244px"><span class="dot"><svg width="10" height="10" viewBox="0 0 10 10" fill="#aeb4ba"><path d="M2 0l2 2.5-1 1.2a6 6 0 0 0 3.3 3.3l1.2-1L10 8 8.5 10C4 10 0 6 0 1.5z"/></svg></span>01632 960418</div>

  <div class="foot-col" style="left:463px">
    <h4>ABOUT</h4>
    <a>Meet The Team</a><a>Our Values</a><a>Software Solutions</a><a>Vacancies</a>
  </div>
  <div class="foot-col" style="left:662px">
    <h4>SERVICES</h4>
    <a>Company Services</a><a>Personal Services</a><a>Advisory Services</a>
  </div>
  <div class="foot-col" style="left:863px">
    <h4>WHO WE HELP</h4>
    <a>Property Investors and Developers</a><a>Consultants</a><a>Medical Professionals</a><a>Buying or Selling a Business</a>
  </div>

  <div class="foot-bottom">
    <span class="copyright">Copyright © 2023 tolvardaccountants. All rights reserved</span>
    <span class="badge-a" role="img" aria-label="Professional membership badge"></span>
    <span class="badge-b" role="img" aria-label="Accreditation badge"></span>
    <div class="social"><span></span><span></span><span></span><span></span></div>
  </div>
</footer>

</body>
</html>
```